ORLUq Business card. A.I. company developing trading strategies.

My name is tommaso fabbri and I'm CEO and co-founder of ORLUQ Research, an AI company focusing on generating Ai-driven trading strategies.
This is our website: https://orluq-research.example/
Values of our company: tech & R&D driven (we're all very mathy/stats/data driven), sophisticated (we only look for sophisticated, high knowledge investors), reserved (we don't go around telling anyone what we do).
Our main product: KobraFNX. A trading strategy that delivered 70% in 2022 and 20% in 2023 so far.
Our main potential clients: HNW individuals, hedge funds, asset managers, tech entrepreneur.
Hedge funds, asset managers, High Net Worth individuals, Pension funds
The basic: name, job title, company name, address, mail, phone number

```html
<!DOCTYPE html>
<html lang="en">
<head>
<meta charset="utf-8">
<title>ORLUq Research – Business Card</title>
<link rel="stylesheet" href="https://fonts.googleapis.com/css2?family=Raleway:wght@300;400;700&display=swap">
<style>
  :root {
    --backdrop: #d0d0d0;
    --card-dark-start: #121315;
    --card-dark-end: #2a2d32;
    --card-light: #ffffff;
    --ink: #262626;
    --ink-soft: #555555;
    --accent: #a8263a;
    --white: #ffffff;
  }
  * { margin: 0; padding: 0; box-sizing: border-box; }
  html, body {
    width: 1200px; height: 1000px; overflow: hidden;
    background: var(--backdrop);
    font-family: "Raleway", sans-serif;
  }
  .canvas { position: relative; width: 1200px; height: 1000px; }
  .card {
    position: absolute; left: 293px; width: 613px; height: 352px;
    box-shadow: 0 18px 40px rgba(0,0,0,0.28);
  }
  .card--front {
    top: 118px;
    background: linear-gradient(90deg, var(--card-dark-start) 0%, var(--card-dark-start) 18%, var(--card-dark-end) 55%, #2e3136 100%);
  }
  .card--back { top: 525px; background: var(--card-light); }

  .wordmark {
    position: absolute; left: 0; right: 0;
    display: flex; justify-content: center; align-items: center; gap: 8px;
    font-weight: 300; font-size: 46px; letter-spacing: 4px; line-height: 1;
  }
  .wordmark__dot { width: 6px; height: 6px; border-radius: 50%; background: var(--accent); }
  .card--front .wordmark { top: 150px; color: var(--white); }
  .card--back .wordmark { top: 45px; color: var(--ink); }

  .person {
    position: absolute; right: 320px; top: 177px; text-align: right;
  }
  .person__name {
    color: var(--accent); font-weight: 700; font-size: 22px;
    text-transform: uppercase; line-height: 1.1;
  }
  .person__title {
    color: var(--ink-soft); font-size: 11.5px; letter-spacing: 1px;
    text-transform: uppercase; margin-top: 3px;
  }
  .divider {
    position: absolute; left: 306px; top: 168px; width: 2px; height: 55px;
    background: var(--accent);
  }
  .contacts {
    position: absolute; left: 317px; top: 166px; list-style: none;
    color: var(--ink); font-size: 16px; line-height: 19px;
  }
  .contacts__item { display: flex; align-items: center; gap: 6px; }
  .contacts__icon { width: 13px; height: 13px; flex: none; fill: var(--accent); }
  .address {
    position: absolute; left: 0; right: 0; top: 315px; text-align: center;
    color: var(--ink); font-size: 16px;
  }
</style>
</head>
<body>
<main class="canvas">
  <section class="card card--front">
    <div class="wordmark"><span>ORLUq Research</span><span class="wordmark__dot"></span></div>
  </section>

  <section class="card card--back">
    <div class="wordmark"><span>ORLUq Research</span><span class="wordmark__dot"></span></div>

    <div class="person">
      <p class="person__name">Tommaso Fabbri</p>
      <p class="person__title">CEO and Co-Founder</p>
    </div>
    <div class="divider"></div>
    <ul class="contacts">
      <li class="contacts__item">
        <svg class="contacts__icon" viewBox="0 0 16 16"><path d="M1 6c0-2 3-3 7-3s7 1 7 3v1h-4V5.5H5V7H1z"/><path d="M4 8h8l2 6H2z"/><circle cx="8" cy="11" r="1.6" fill="#fff"/></svg>
        <span>600 555 0142</span>
      </li>
      <li class="contacts__item">
        <svg class="contacts__icon" viewBox="0 0 16 16"><path d="M1 4h14v9H1z"/><path d="M1 4l7 5 7-5" fill="none" stroke="#fff" stroke-width="1.4"/></svg>
        <span>office@orluqresearch.example</span>
      </li>
      <li class="contacts__item">
        <svg class="contacts__icon" viewBox="0 0 16 16"><circle cx="8" cy="8" r="6.5"/><path d="M1.5 8h13M8 1.5c-3 3-3 10 0 13M8 1.5c3 3 3 10 0 13M2.5 5h11M2.5 11h11" fill="none" stroke="#fff" stroke-width="0.9"/></svg>
        <span>orluqresearch.example</span>
      </li>
    </ul>

    <p class="address">14 rue des Lilas 75003 Paris</p>
  </section>
</main>
</body>
</html>
```